Basic loan proposal for mortgage broker needs wow factor design in Word

I have a basic word template that is quite ugly. I would like a designer to make it wow!

There are merge fields all over it and they need to be in there

My website is www.trelbyloans.com.au for logo

Home Loans

Home Loans

```html
<!DOCTYPE html>
<html lang="en">
<head>
<meta charset="utf-8">
<title>Preliminary Assessment &amp; Credit Proposal – Page Layouts</title>
<link rel="stylesheet" href="https://fonts.googleapis.com/css2?family=Arimo:wght@400;700&family=Roboto+Condensed:wght@700&display=swap">
<style>
:root{
  --backdrop:#aaa7a8;
  --paper:#ffffff;
  --ink:#1a1a1a;
  --band:#1c1c1c;
  --band-text:#ffffff;
  --shade:#d5d5d5;
  --rule:#a9a9a9;
  --accent-bar:#8c8c8c;
}
*{box-sizing:border-box;margin:0;padding:0}
html,body{width:1200px;height:3819px;overflow:hidden;background:var(--backdrop)}
body{position:relative;font-family:"Arimo",Arial,sans-serif;color:var(--ink);font-size:7px;line-height:1.3}
.page{position:absolute;width:483px;height:683px;background:var(--paper);padding:30px 30px 0;overflow:hidden}
.logo{font-family:"Roboto Condensed","Arial Narrow",sans-serif;font-weight:700;font-size:36px;line-height:1;letter-spacing:-.5px;color:var(--ink)}
.page.right .logo{text-align:right}
.page-title{font-size:14px;text-align:center;letter-spacing:.3px;margin:14px 0 7px}
.bar{background:var(--band);color:var(--band-text);font-weight:700;font-size:7.5px;text-transform:uppercase;letter-spacing:.2px;height:13px;line-height:13px;padding:0 7px;margin-top:9px}
.shade{background:var(--shade);font-size:6.5px;text-transform:uppercase;height:13px;line-height:13px;padding:0 7px;margin-top:7px;color:#444}
.rules{background:repeating-linear-gradient(to bottom,transparent 0 10px,var(--rule) 10px 11px)}
.para{margin-top:5px;font-size:6.8px}
.note{margin-top:7px;padding-left:9px;font-size:6.5px}
.field{border-bottom:1px solid var(--rule);height:13px;line-height:15px;font-size:6.8px;display:flex}
.field span{flex:1}
.field span+span{border-left:1px solid var(--rule);padding-left:3px}
.item{border-bottom:1px solid var(--rule);height:17px;line-height:22px;font-size:6.8px}
.folio{position:absolute;bottom:12px;font-size:6.5px}
.folio b{font-weight:700}
.page.left .folio{left:30px}
.page.right .folio{right:30px}
ul.dots{list-style:none;font-size:6.8px}
ul.dots li::before{content:"• "}
/* cover */
.cover-head{display:flex;height:125px;margin:-30px 0 0}
.cover-head .logo{font-size:68px;padding-top:42px;width:170px}
.cover-rule{width:8px;background:var(--accent-bar);height:125px;margin-right:30px}
.cover-title{padding-top:42px;font-weight:700;font-size:28px;line-height:1.05}
.cover-title small{display:block;font-weight:400;font-size:19px;margin-top:2px}
.issue{margin-top:44px;border-bottom:1px solid var(--rule);font-size:6.8px;height:11px}
.section-title{font-size:14px;text-align:center;margin:22px 0 12px}
.checks .check{display:flex;align-items:center;gap:18px;margin:10px 0 0 18px;font-size:6.8px}
.box{width:21px;height:21px;border:1.5px solid #555;flex:none}
.or{margin:4px 0 0 75px;font-size:6.8px}
.sign{border-bottom:1px solid var(--rule);height:18px;margin-top:20px;font-size:6.8px;line-height:24px}
.commission-table{margin-top:14px;width:100%;border-collapse:collapse}
.commission-table td{border:1px solid #888;height:13px}
.appendix{font-size:14px;text-align:center;margin:22px 0 4px}
.entry{border-bottom:1px solid var(--rule);height:18px;line-height:24px;font-size:6.8px}
</style>
</head>
<body>

<!-- Page 1: cover -->
<section class="page right" style="left:604px;top:108px">
  <header class="cover-head">
    <div class="logo">LOGO</div>
    <div class="cover-rule"></div>
    <h1 class="cover-title">PRELIMINARY<br>ASSESSMENT<small>&amp; CREDIT PROPOSAL</small></h1>
  </header>
  <div class="issue">Issue date:</div>
  <div class="bar">About you</div>
  <div class="rules" style="height:46px"></div>
  <div class="bar" style="margin-top:16px">About us</div>
  <div class="shade">Broker details</div>
  <div class="field"><span>Broker:</span></div>
  <div class="field"><span>Credit Representative Name:</span></div>
  <div class="field"><span>Credit Representative Number:</span><span style="flex:.75">Member Number:</span></div>
  <div class="field"><span>Business Name:</span></div>
  <div class="field"><span>Address:</span></div>
  <div class="field"><span>Phone Number:</span></div>
  <div class="field"><span>Email:</span></div>
  <div class="shade">Licensee details</div>
  <div class="field"><span>Australian Credit Licence Name:</span></div>
  <div class="field"><span>Australian Credit Licence Number:</span></div>
  <div class="field"><span>Business Name:</span></div>
  <div class="field"><span>Address:</span></div>
  <div class="field"><span>Phone Number:</span></div>
  <div class="field"><span>Email:</span></div>
  <p class="para" style="margin-top:9px">If your Broker is a Credit Representative, this Preliminary Assessment &amp; Credit Proposal is being provided on behalf of the Licensee.</p>
  <div class="bar">About this preliminary assessment &amp; credit proposal</div>
  <p class="para">This Preliminary Assessment &amp; Credit Proposal sets out important information that we must give you when we provide you with credit assistance.</p>
  <p class="para">This document outlines:</p>
  <ul class="dots">
    <li>the information provided by you in relation to your financial situation, requirements and objectives;</li>
    <li>the preliminary assessment we completed to ensure we recommended a loan which is not unsuitable for you;</li>
    <li>our recommendation and why we believe this is in your best interests;</li>
    <li>fees and charges payable; and</li>
    <li>commissions that we or other parties may receive in relation to the proposed loan/s.</li>
  </ul>
  <p class="para">Please read through and sign the Client Acknowledgement to indicate that the content is true and correct at the time of signing.</p>
  <div class="folio"><b>PRELIMINARY ASSESSMENT</b> &amp; CREDIT PROPOSAL &nbsp; 1</div>
</section>

<!-- Page 2 -->
<section class="page left" style="left:120px;top:840px">
  <div class="logo">LOGO</div>
  <h2 class="page-title">PRELIMINARY ASSESSMENT</h2>
  <div class="bar" style="margin-top:0">Assessment details</div>
  <p class="para">We have based this assessment on the information provided by you in the Client Needs Analysis. We have assessed that this particular credit application is NOT UNSUITABLE for you. This assessment is valid for 90 days from the date it has been issued.</p>
  <div class="bar">Monthly financial position</div>
  <p class="para">A summary of your current versus proposed monthly financial position (including a buffer/floor rate) is set out below. The calculations are based on the information you provided and we verified.</p>
  <div class="rules" style="height:22px"></div>
  <p class="note">• Buffer is calculated as: 80.00% of rental income added to gross income, 3.00% buffer or current mortgage rates, 5.25% as floor rate on proposed loan rates.</p>
  <div class="bar">Needs &amp; objectives</div>
  <div class="shade" style="margin-top:5px">Primary reasons for seeking credit/your needs &amp; objectives</div>
  <div class="rules" style="height:44px"></div>
  <div class="shade" style="height:24px;line-height:1.3;padding-top:3px">Immediate needs &amp; objectives - within the next two years (e.g. holiday, purchases, renovations, savings, protect the family, etc.)</div>
  <div class="rules" style="height:44px"></div>
  <div class="shade" style="height:24px;line-height:1.3;padding-top:3px">Longer term - between 2 to 10 years' time (e.g. repay mortgage, buy a new car, education expenses, purchase investment property, retirement planning, etc)</div>
  <div class="bar">Requirements &amp; objectives</div>
  <div class="rules" style="height:55px"></div>
  <div class="bar" style="margin-top:16px">Product requirements</div>
  <p class="para">This is a summary of the specific loan features you have requested. Please ensure you have read and understood the characteristics associated with each feature.</p>
  <div class="rules" style="height:44px"></div>
  <div class="folio"><b>2 &nbsp; PRELIMINARY ASSESSMENT</b> &amp; CREDIT PROPOSAL</div>
</section>

<!-- Page 3 -->
<section class="page right" style="left:605px;top:840px">
  <div class="logo">LOGO</div>
  <div class="bar" style="margin-top:18px">Broker disclosure</div>
  <div class="rules" style="height:33px"></div>
  <p class="note">* Please refer to the Risks/Benefits Statements which covers the risks and benefits of your requested loan features.</p>
  <div class="bar">What is most important for you?</div>
  <div class="rules" style="height:66px"></div>
  <div class="bar">Term of credit sought</div>
  <div class="rules" style="height:55px"></div>
  <div class="bar" style="margin-top:14px">Broker analysis</div>
  <div class="shade" style="margin-top:5px">Analysis, assessment and applicant education comments</div>
  <div class="rules" style="height:44px"></div>
  <div class="bar" style="margin-top:18px">Loan products/features compared</div>
  <p class="para">Based on the information provided by you, we compared the following lenders and products before making our recommendation:</p>
  <div class="rules" style="height:143px"></div>
  <p class="note">* Lenders Mortgage Insurance (LMI) is allocated to the primary 'split' of the proposed loan product.<br>&nbsp;&nbsp;This allocation may vary in accordance with your requirements and/or the lender's credit criteria.</p>
  <div class="rules" style="height:55px"></div>
  <p class="note">* The above chart shows the principal, interest and fees payable for the compared loan/s.</p>
  <div class="folio"><b>PRELIMINARY ASSESSMENT</b> &amp; CREDIT PROPOSAL &nbsp; 3</div>
</section>

<!-- Page 4 -->
<section class="page left" style="left:120px;top:1569px">
  <div class="logo">LOGO</div>
  <h2 class="page-title">CREDIT PROPOSAL</h2>
  <div class="bar" style="margin-top:0">Loan products/features recommended</div>
  <p class="para">Based on your circumstances and the features relevant to your requirements and objectives, we recommend the following lender and product:</p>
  <div class="rules" style="height:55px"></div>
  <p class="note">* Interest rates, fees and repayments may change if the lender changes its loan terms.</p>
  <div class="rules" style="height:22px"></div>
  <p class="note">* If an offset account is available for your recommended loan/s, the above graph compares a loan operating without an offset account against a loan linked with an offset account. This calculation is based on your initial offset balance and estimated monthly offset contribution.</p>
  <div class="shade">Product suitability</div>
  <div class="rules" style="height:33px"></div>
  <div class="bar">Why our recommendation meets your best interests</div>
  <div class="shade" style="margin-top:3px">Options presented and recommendation comments</div>
  <div class="rules" style="height:22px"></div>
  <div class="shade">Explanation for selecting interest only repayment <i>(if applicable)</i></div>
  <div class="rules" style="height:22px"></div>
  <div class="shade">Explanation for selecting fixed rate product <i>(if applicable)</i></div>
  <div class="rules" style="height:22px"></div>
  <div class="shade">Line of credit comments <i>(if applicable)</i></div>
  <div class="rules" style="height:22px"></div>
  <div class="shade">Interest in advance comments <i>(if applicable)</i></div>
  <div class="rules" style="height:22px"></div>
  <div class="shade">Conflict of interest disclosure</div>
  <div class="rules" style="height:22px"></div>
  <div class="shade">Security to be provided by you</div>
  <div class="rules" style="height:22px"></div>
  <div class="folio"><b>4 &nbsp; PRELIMINARY ASSESSMENT</b> &amp; CREDIT PROPOSAL</div>
</section>

<!-- Page 5 -->
<section class="page right" style="left:605px;top:1569px">
  <div class="logo">LOGO</div>
  <div class="shade" style="margin-top:18px">Funding worksheet</div>
  <div class="rules" style="height:66px"></div>
  <p class="note">* If you are refinancing, please refer to the Refinance Analysis which considers the costs of a refinance with the<br>&nbsp;&nbsp;benefits you could receive from your proposed loan/s.</p>
  <div class="bar">Estimated fees &amp; charges payable by you for your loan/s</div>
  <p class="para">An estimate of the total fees and charges that may be payable by you to the lender in relation to applying for the loan/s are listed in the table below:</p>
  <div class="rules" style="height:44px"></div>
  <p class="note">* These fees and charges are one-off payments unless otherwise indicated. These amounts are estimates only and the final figures will be shown in the credit contract issued by the lender. Some or all of these fees and charges may be payable from the loan proceeds.</p>
  <div class="bar">Estimated fees payable by you to us</div>
  <p class="para">If a fee is payable by you, this will have been disclosed in the Credit Quote we have previously given to you. The Credit Quote will outline any fees payable for providing credit assistance and the time that they are payable. If you did not receive a Credit Quote, this will indicate that no fees are payable.</p>
  <div class="bar">How are we paid?</div>
  <p class="para">We are remunerated by commission from your recommended lender and this is generally by way of both an upfront and trail commission based on your loan amount.</p>
  <p class="para">Upfront commission is a one-off commission paid after settlement with a maximum upfront commission of 1.5%.</p>
  <p class="para">Trail commission is an ongoing commission paid generally over the life of the loan and is based on the monthly balance of your loan amount. This commission is a maximum of 0.5% per annum.</p>
  <p class="para">Commissions are paid based on a percentage of the loan drawn down in most cases net of any offset amount. The way commissions are calculated and paid to us by lenders may vary. By following the responsible lending and best interests obligations, we will ensure that the loan/s recommended to you is not unsuitable to your requirements and objectives.</p>
  <p class="para">These commissions may be shared between [organization.license.institution1], the Broker and any referring party (as disclosed in this Preliminary Assessment &amp; Credit Proposal).</p>
  <p class="para">We are not eligible for volume bonuses in relation to the loan/s.</p>
  <div class="bar">Other fees/benefits we may be entitled to be paid</div>
  <p class="para">Other benefits may be received from our panel of lenders from time to time. These benefits may include benefits such as attendance at social events, higher servicing standards from lenders and training and educational opportunities.</p>
  <p class="para">You are entitled to ask your Broker if any additional fees or benefits may be applicable to your credit application.</p>
  <div class="folio"><b>PRELIMINARY ASSESSMENT</b> &amp; CREDIT PROPOSAL &nbsp; 5</div>
</section>

<!-- Page 6 -->
<section class="page left" style="left:120px;top:2299px">
  <div class="logo">LOGO</div>
  <div class="bar" style="margin-top:18px">Reasonable estimate of commission</div>
  <p class="para">An estimate of commission to be received by the Licensee from the lender for assisting you to obtain the finance are listed in the table below.</p>
  <p class="para">We may receive an upfront commission, payable shortly after settlement.</p>
  <p class="para">We also receive a monthly commission calculated as the percentage of the outstanding loan balance. Details of these commissions are listed in the table below.</p>
  <p class="para">An estimate of referral fees payable by us to any third parties are also listed in the table below.</p>
  <table class="commission-table">
    <tr><td></td><td></td></tr><tr><td></td><td></td></tr><tr><td></td><td></td></tr><tr><td></td><td></td></tr><tr><td></td><td></td></tr>
  </table>
  <div class="bar" style="margin-top:14px">Additional commentary relevant to your circumstances</div>
  <div class="shade" style="margin-top:3px">Borrowing power commentary</div>
  <div class="rules" style="height:44px"></div>
  <div class="shade">Deposit/equity comments</div>
  <div class="rules" style="height:44px"></div>
  <div class="shade">Credit history comments</div>
  <div class="rules" style="height:44px"></div>
  <div class="shade">Security (property) notes</div>
  <div class="rules" style="height:44px"></div>
  <div class="shade">Living expenses comments</div>
  <div class="rules" style="height:44px"></div>
  <div class="folio"><b>6 &nbsp; PRELIMINARY ASSESSMENT</b> &amp; CREDIT PROPOSAL</div>
</section>

<!-- Page 7 -->
<section class="page right" style="left:605px;top:2299px">
  <div class="logo">LOGO</div>
  <h2 class="section-title" style="margin-top:18px">INSURANCE DECLARATION</h2>
  <p class="para">To ensure we have taken the appropriate duty of care when arranging finance on your behalf, we must make you aware of the need to protect yourself, your family and your business from the possible financial hardship caused by death, disability, trauma or personal injury.</p>
  <p class="para">If you do not have adequate risk insurance in place, you may not be able to make the repayments on your loan/s if you had an accident or illness that stopped you working, or in the event of permanent disability or death. It is important that you understand the risks of not maintaining sufficient insurance to protect your loan/s and your assets.</p>
  <div class="checks">
    <div class="check"><span class="box"></span>I/We acknowledge that my/our Broker has brought this to our attention</div>
    <div class="check"><span class="box"></span>I/We understand that insurance is not compulsory and is not a condition of the loan/s being approved</div>
    <div class="check"><span class="box"></span>I/We have considered the risks and are satisfied with the current level of personal insurance protection or<br>have made my/our own arrangements</div>
    <div class="or">OR</div>
    <div class="check" style="margin-top:4px"><span class="box"></span>I/We have considered the risks and would like to discuss the insurance options with someone<br>recommended by my/our Broker</div>
  </div>
  <h2 class="section-title" style="margin-top:40px">CLIENT ACKNOWLEDGEMENT</h2>
  <p class="para">By signing this Preliminary Assessment &amp; Credit Proposal, you agree and acknowledge that this assessment is based on the requirements and objectives, income and expenses which you have provided to [organization.license.institution1].</p>
  <p class="para">You should check carefully that the information provided in this document and its appendices is accurate and up-to-date and that there is no omissions or inaccuracies (including any foreseeable changes to your financial situation) which may impact on your ability to meet the payment requirements in the credit contract for which you have applied.</p>
  <div class="sign" style="margin-top:34px">Signature:</div>
  <div class="sign">Signature:</div>
  <div class="sign">Signature:</div>
  <div class="folio"><b>PRELIMINARY ASSESSMENT</b> &amp; CREDIT PROPOSAL &nbsp; 7</div>
</section>

<!-- Page 8 -->
<section class="page left" style="left:125px;top:3030px">
  <div class="logo">LOGO</div>
  <h2 class="appendix" style="margin-top:18px">APPENDIX 1:</h2>
  <div class="bar" style="margin-top:0">Risk/benefits statements</div>
  <div class="entry" style="height:15px;line-height:18px">Documents Risk Benefit</div>
  <h2 class="appendix" style="margin-top:26px">APPENDIX 2:</h2>
  <div class="bar" style="margin-top:0">Refinance analysis</div>
  <div class="entry">Refinance Analysis</div>
  <div class="entry">Refinance Analysis Benefit</div>
  <div class="entry">Refinance Analysis Additional Monthly Repayment</div>
  <div class="entry">Refinance Analysis Reasons</div>
  <p class="note">* If you are not refinancing, this Refinance Analysis has been intentionally left blank.</p>
  <h2 class="appendix" style="margin-top:20px">APPENDIX 3:</h2>
  <div class="bar" style="margin-top:0">Client needs analysis</div>
  <div class="shade" style="margin-top:3px">Personal details</div>
  <div class="entry" style="margin-top:8px">General Details</div>
  <div class="entry">Contact Details</div>
  <div class="entry">Address Details</div>
  <div class="entry">Identification</div>
  <div class="entry">Family Relations</div>
  <div class="entry">Next of Kin</div>
  <div class="shade" style="margin-top:12px">Employment details</div>
  <div class="entry" style="margin-top:6px">Current Employment</div>
  <div class="entry">Previous Employment</div>
  <div class="shade" style="margin-top:12px">Income</div>
  <div class="entry">Annual income summary</div>
  <div class="folio"><b>8 &nbsp; PRELIMINARY ASSESSMENT</b> &amp; CREDIT PROPOSAL</div>
</section>

<!-- Page 9 -->
<section class="page right" style="left:605px;top:3030px">
  <div class="logo">LOGO</div>
  <div class="shade" style="margin-top:18px">Expenses</div>
  <div class="entry" style="height:14px;line-height:16px">Expenses by Household with comments</div>
  <div class="shade" style="margin-top:18px">Assets</div>
  <div class="entry" style="height:14px;line-height:16px">Assets</div>
  <div class="shade" style="margin-top:18px">Liabilities</div>
  <div class="entry" style="height:14px;line-height:16px">Liabilities extended</div>
  <p class="note" style="margin-top:3px">* The credit card monthly repayment is calculated at a rate of 3.8% of the credit card limit.</p>
  <div class="shade" style="margin-top:14px">Insurers</div>
  <div class="entry" style="height:14px;line-height:16px">Insurance Providers</div>
  <div class="shade" style="margin-top:18px">Other advisers</div>
  <div class="entry" style="height:14px;line-height:16px">Other Advisers</div>
  <div class="shade" style="margin-top:18px">Possible changes to financial situation</div>
  <div class="entry" style="height:14px;line-height:16px">Changes in Financial situation</div>
  <div class="entry" style="height:18px;line-height:22px">Beneficial Changes in Financial situation</div>
  <div class="shade" style="margin-top:18px">Exit strategy</div>
  <div class="entry" style="height:14px;line-height:16px">Exit Strategy</div>
  <div class="shade" style="margin-top:18px">Your financial security</div>
  <div class="entry" style="height:14px;line-height:16px">Your Financial Security New</div>
  <div class="shade" style="margin-top:18px">Your credit history</div>
  <div class="entry" style="height:14px;line-height:16px">Your Credit History New</div>
  <div class="shade" style="margin-top:18px">Verifications completed</div>
  <div class="entry" style="height:14px;line-height:16px">Interview Details</div>
  <div class="entry" style="height:18px;line-height:22px">Verifications Completed</div>
  <div class="folio"><b>PRELIMINARY ASSESSMENT</b> &amp; CREDIT PROPOSAL &nbsp; 9</div>
</section>

</body>
</html>
```